Packaging Design for Vorimelt a Company Providing a Convenient and Complete Alternative to Food

We need a packaging and label design for Vorimelt. Vorimelt stands for nutrient balance and it is a meal alternative that comes in a powder that has all the nutrients needed for a complete and balanced meal. Vorimelt would be used by people that are hungry but don't have time to cook, are in a rush, or simply want to get the healthiest meal they can as conveniently as possible. We were thinking of using a modern and simple design that would attract consumers in the 22-28 age bracket. I want the packaging to be cool and attractive using blue and orange/red (an orangey red) since those are the colors of the logo

Now that being said, Vorimelt is more about a lifestyle than the product itself. The website still doesn't reflect this because the first step for me in creating it was to put in all the hard info and facts and then slowly transform it to what I want it to be. Vorimelt's "slogan" is spark every hour and the idea is that the product will be used by people who are busy having too much fun in life so they don't have time to cook so they choose to have Vorimelt. For example a commercial we are producing starts with first person footage of me getting in a skyvane 40 and then doing all sorts of water sports and having fun in the beach. At the end, there's a hot girl in a boat making a vorimelt and drinking it. So as you can see it's not about the product itself but what we want people to feel when they think about it and part of what they feel will be conveyed by the logo.

I want to convey a sense of energy and fun. I want people to feel inspired and feel something when they see the packaging since this is the same logo that will go on the product packaging (I will hold another project for that as soon as this one ends).

Our target market is a young professional probably with higher disposable income than your average 24-35 year old, trendy, modern, sophisticated and often consumes premium brands and therefore the packaging must reflect that.

The bottle will use a shrink sleeve that will wrap around from the bottom of the bottle up to the neck. The bottle is white, with a white smooth cap. I want the design to be able to blend in with the white of the bottle so that it all flows. I was thinking of maybe leaving some parts transparent so that the white of the bottle shows instead of using white but I honestly don't know if that would be a good idea.

Attached you will find the template for the shrink sleeve, the logo and the tub. The picture of the bottle is only a reference so that you can know what size it will be.

I'm going to need the design both in the template and on the tub. Make it look nice since I might be using the designs as a background in the website and definitely as the product image (what people will be clicking on to buy it)

Here are the things that need to be on the tub (these will be modified later only to be used as a placeholder for now):

Under the logo or in the front and middle of the tub (under Vorimelt probably):
A Complete and Balanced Meal Alternative.

It needs to say its vanilla flavored

It needs to have the supplement facts (just put any random numbers)

Directions: Use 2-4 scoops depending on your level of hunger. Mix 5 ounces of water per scoop in a thermos, shaker cup, or closed bottle and shake vigorously for ten seconds. Drink and enjoy!

What is Vorimelt?
Vorimelt is a complete and balanced meal alternative that gives your body all the right nutrients to keep it functioning at its full potential. Vorimelt will nourish your body with good proteins, carbohydrates, fats, and micro-nutrients (like vitamins and minerals) so that you don't have to worry about cooking or eating the right stuff. We take care of everything for you so that you can keep on doing what you love, whatever that may be. Vorimelt will spark every hour!
For more information go to Vorimelt.example

Hey i forgot to add that its gonna be vanilla flavored

```html
<!DOCTYPE html>
<html lang="en">
<head>
<meta charset="utf-8">
<title>Vorimelt Shrink Sleeve – Vanilla</title>
<link href="https://fonts.googleapis.com/css2?family=Arimo:wght@400;700&display=swap" rel="stylesheet">
<style>
  :root {
    --ink: #231f20;
    --brand-blue: #1c6db5;
    --brand-orange: #ec5a24;
    --guide-red: #e8403a;
    --guide-pink: #f19aa0;
    --guide-blue: #2a6fb7;
    --no-ink-grey: #bcbec0;
    --note-yellow: #fff200;
    --paper: #ffffff;
  }
  * { box-sizing: border-box; margin: 0; padding: 0; }
  html, body { width: 1200px; height: 604px; overflow: hidden; background: var(--paper); }
  body { position: relative; font-family: "Arimo", Arial, sans-serif; color: var(--ink); }
  .abs { position: absolute; }
  .guides { position: absolute; inset: 0; }

  .spec-list { left: 4px; top: 4px; font-size: 8px; line-height: 10.4px; }
  .clear-key { left: 228px; top: 0; width: 25px; height: 20px; background: var(--no-ink-grey); }
  .clear-key-label { left: 262px; top: 8px; font-size: 6px; }
  .red-note { color: var(--guide-red); font-size: 7.5px; line-height: 9px; text-align: center; }
  .blue-note { color: var(--guide-blue); font-size: 6px; line-height: 7.5px; text-align: center; }
  .dim { font-size: 8px; background: var(--paper); padding: 0 3px; }
  .fold-label { font-size: 6px; color: #777; transform: rotate(-90deg); }

  .template-note {
    left: 0; top: 307px; width: 180px; height: 268px; background: var(--note-yellow);
    color: var(--guide-red); font-size: 8px; line-height: 10.6px; padding: 12px 8px;
  }
  .template-note p + p { margin-top: 21px; }
  .barcode-note { left: 93px; top: 281px; font-size: 5px; line-height: 6px; }

  .copy-panel { left: 197px; top: 238px; width: 176px; font-size: 9.4px; line-height: 12px; }
  .copy-panel h2 { font-size: 9.6px; font-weight: 700; margin-bottom: 2px; }
  .copy-panel p { margin-bottom: 16px; }
  .copy-panel .web { margin-top: -2px; }

  .brand-name {
    left: 440px; top: 214px; width: 340px; text-align: center;
    font-size: 32px; letter-spacing: 2px; color: var(--brand-blue);
  }
  .brand-dot { left: 560px; top: 285px; width: 96px; height: 96px; border-radius: 50%; background: var(--brand-orange); }
  .claim { left: 440px; top: 457px; width: 340px; text-align: center; font-size: 12.5px; }
  .flavour { left: 440px; top: 474px; width: 340px; text-align: center; font-size: 17px; letter-spacing: .5px; }
  .net-weight { left: 440px; top: 513px; width: 340px; text-align: center; font-size: 9.5px; }

  .facts-box {
    left: 906px; top: 228px; width: 127px; height: 129px;
    border: 2px solid var(--brand-blue); border-radius: 4px; padding: 4px 5px; font-size: 5px; line-height: 5.8px;
  }
  .facts-box h3 { font-size: 5.5px; font-weight: 700; }
  .facts-box table, .amino-box table { width: 100%; border-collapse: collapse; margin-top: 4px; }
  .facts-box td, .amino-box td { font-size: 4.3px; line-height: 5.3px; }
  .facts-box td:not(:first-child) { text-align: right; }
  .facts-box .foot { margin-top: 5px; font-size: 3.8px; line-height: 4.6px; }
  .amino-box {
    left: 922px; top: 368px; width: 112px; height: 118px;
    border: 2px solid var(--brand-orange); border-radius: 4px; padding: 3px 5px; font-size: 5px;
  }
  .amino-box h3 {
    background: var(--brand-orange); color: var(--paper); font-size: 4.8px; font-weight: 700;
    padding: 1px 3px; margin: 0 -3px;
  }
  .amino-box table { margin-top: 6px; }
  .amino-box td { line-height: 4.95px; padding-left: 5px; }
  .amino-box td:last-child { text-align: right; padding-right: 14px; }

  .image-area-label { left: 1140px; top: 300px; width: 40px; text-align: center; font-size: 8px; line-height: 11px; }
  .height-label { left: 1173px; top: 310px; font-size: 8px; transform: rotate(-90deg); }
</style>
</head>
<body>

<div class="abs spec-list">
  8/18/14<br>Template No. 10,932.0<br>Capworks<br>3000cc Quick Meal<br>242mmLF x 238.125mmCL<br>492mm Slit Width<br>487mm Image Width<br>234.125mm Image Height<br>150T • 2 Around<br>HSPVC<br>Cut Bands
</div>
<div class="abs clear-key"></div>
<div class="abs clear-key-label">Clear: No ink in this area</div>

<div class="abs red-note" style="left:470px;top:16px;width:260px;font-size:6.5px;line-height:8px">492mm (19.3701") x 238.125mm (9.375") overall<br>487mm x 234.125mm graphics area</div>
<div class="abs red-note" style="left:160px;top:21px;width:50px">1mm<br>no ink</div>
<div class="abs red-note" style="left:1110px;top:21px;width:50px">4mm<br>no ink</div>
<div class="abs red-note" style="left:800px;top:38px;width:72px;font-size:6.5px;line-height:8px">T-Perf<br>38mm from top<br>6mm from fold</div>
<div class="abs red-note" style="left:104px;top:93px;width:70px;font-size:6.5px">12mm Cap Overlap</div>
<div class="abs red-note" style="left:100px;top:180px;width:78px;font-size:6.5px;line-height:8px">30mm Shoulder Area<br>High Distortion</div>
<div class="abs red-note" style="left:112px;top:512px;width:66px;font-size:6.5px;line-height:8px">25mm Radius<br>High Distortion</div>
<div class="abs red-note" style="left:1145px;top:84px;width:50px;font-size:6px">2mm no ink</div>
<div class="abs red-note" style="left:1145px;top:540px;width:50px;font-size:6px">2mm no ink</div>

<div class="abs blue-note" style="left:150px;top:576px;width:70px">5mm for<br>seam underlap<br>Background Graphics Only<br>NO TEXT THIS AREA</div>
<div class="abs blue-note" style="left:1085px;top:576px;width:70px">1mm for<br>seam underlap<br>Background Graphics Only<br>NO TEXT THIS AREA</div>

<svg class="guides" width="1200" height="604" viewBox="0 0 1200 604" aria-hidden="true">
  <g stroke="var(--ink)" stroke-width=".7" fill="none">
    <line x1="182" y1="76" x2="1133" y2="76"/>
    <path d="M186 73 L182 76 L186 79 M371 73 L375 76 L371 79 M379 73 L375 76 L379 79 M832 73 L836 76 L832 79 M840 73 L836 76 L840 79 M1129 73 L1133 76 L1129 79"/>
  </g>
  <g stroke="var(--guide-pink)" stroke-width=".8" stroke-dasharray="3 2" fill="none">
    <line x1="181" y1="48" x2="181" y2="565"/>
    <line x1="375" y1="48" x2="375" y2="545"/>
    <line x1="836" y1="60" x2="836" y2="545"/>
    <line x1="830" y1="90" x2="830" y2="157"/>
    <line x1="848" y1="90" x2="848" y2="157"/>
    <line x1="1118" y1="48" x2="1118" y2="565"/>
    <line x1="1133" y1="48" x2="1133" y2="565"/>
    <line x1="181" y1="108" x2="1133" y2="108"/>
    <line x1="181" y1="157" x2="1133" y2="157"/>
    <line x1="181" y1="215" x2="1133" y2="215"/>
    <line x1="181" y1="500" x2="1133" y2="500"/>
  </g>
  <g stroke="var(--ink)" stroke-width=".6" fill="none">
    <line x1="176" y1="86" x2="176" y2="108"/>
    <line x1="176" y1="157" x2="176" y2="215"/>
    <line x1="176" y1="500" x2="176" y2="545"/>
    <line x1="1180" y1="90" x2="1180" y2="541"/>
    <line x1="1195" y1="86" x2="1195" y2="545"/>
    <line x1="1133" y1="86" x2="1200" y2="86"/>
    <line x1="1133" y1="545" x2="1200" y2="545"/>
  </g>
  <rect x="181" y="85" width="952" height="461" fill="none" stroke="var(--ink)" stroke-width=".6"/>
  <rect x="181" y="86" width="952" height="5" fill="var(--no-ink-grey)"/>
  <rect x="181" y="541" width="952" height="5" fill="var(--no-ink-grey)"/>
  <rect x="1126" y="86" width="7" height="460" fill="var(--no-ink-grey)"/>
  <g stroke="var(--guide-blue)" stroke-width=".8">
    <line x1="185" y1="550" x2="185" y2="572"/>
    <line x1="1120" y1="550" x2="1120" y2="572"/>
  </g>
</svg>

<div class="abs dim" style="left:266px;top:71px">100mm</div>
<div class="abs dim" style="left:592px;top:71px">242mm</div>
<div class="abs dim" style="left:964px;top:71px">150mm</div>
<div class="abs fold-label" style="left:368px;top:553px">fold</div>
<div class="abs fold-label" style="left:829px;top:553px">fold</div>

<div class="abs barcode-note">NOTE:<br>POSITION BARCODE<br>IN THIS DIRECTION</div>

<aside class="abs template-note">
  <p>NOTE: Do not remove or modify any information on this template. All artwork must be submitted with our template number and detailed information. If any modifications are required, please contact us for a revised template.</p>
  <p>Please do not modify the color names (DieLine1, DieLine2) as it will interfere with our proofreading program</p>
</aside>

<section class="abs copy-panel">
  <h2>Directions</h2>
  <p>Use 2-4 scoops depending on your level of hunger. Mix 5 ounces of water per scoop in a thermos, shaker cup, or closed bottle and shake vigorously for ten seconds. Drink and enjoy!</p>
  <h2>What is Vorimelt?</h2>
  <p>Vorimelt is a complete and balanced meal alternative that gives your body all the right nutrients to keep it functioning at its full potential. Vorimelt will nourish your body with good proteins, carbohydrates, fats, and micro-nutrients (like vitamins and minerals) so that you don't have to worry about cooking or eating the right stuff. We take care of everything for you so that you can keep on doing what you love, whatever that may be. Vorimelt will spark every hour!</p>
  <p class="web">For more information go to Vorimelt.example</p>
</section>

<h1 class="abs brand-name" style="font-weight:400">VORIMELT</h1>
<div class="abs brand-dot"></div>
<div class="abs claim">A Complete and Balanced Meal Alternative</div>
<div class="abs flavour">VANILLA</div>
<div class="abs net-weight">NET WT. X00 g</div>

<section class="abs facts-box">
  <h3>NUTRITION FACTS:</h3>
  <div>Serving size: 30g<br>Servings per container: 30<br>Amount per Serving:</div>
  <table>
    <tr><td>Energy Value</td><td>108kcal - 449kJ</td><td>VD/RDI</td></tr>
    <tr><td>Carbohydrate</td><td>1 g</td><td>0 %</td></tr>
    <tr><td>Protein</td><td>24 g</td><td>3 %</td></tr>
    <tr><td>Total Fat</td><td>0.7 g</td><td>31 %</td></tr>
    <tr><td>Saturated Fat</td><td>0.3 g</td><td>1 %</td></tr>
    <tr><td>Trans Fat</td><td>0 g</td><td>0 %</td></tr>
    <tr><td>Dietary Fiber</td><td>0.7 g</td><td>3 %</td></tr>
    <tr><td>Sodium</td><td>100 mg</td><td>8 %</td></tr>
    <tr><td>Calcium</td><td>42 mg</td><td>4 %</td></tr>
    <tr><td>Iron</td><td>5 mg</td><td>30 %</td></tr>
    <tr><td>Magnesium</td><td>12 mg</td><td>5 %</td></tr>
    <tr><td>Potassium</td><td>30 mg</td><td>1 %</td></tr>
  </table>
  <p class="foot">*Daily values based on a 2,000kcal diet or 8,400kJ. Your daily values may be higher or lower depending on your calorie needs. No added sugar. No Lactose.</p>
</section>

<section class="abs amino-box">
  <h3>PROTEIN &amp; AMINO ACIDS</h3>
  <table>
    <tr><td>Alanine</td><td>1.11 g</td></tr>
    <tr><td>Arginine</td><td>1.74 g</td></tr>
    <tr><td>Aspartic acid</td><td>2.54 g</td></tr>
    <tr><td>Cysteine</td><td>0.32 g</td></tr>
    <tr><td>Glutamic acid</td><td>4.52 g</td></tr>
    <tr><td>Glycine</td><td>0.93 g</td></tr>
    <tr><td>Histidine</td><td>0.61 g</td></tr>
    <tr><td>Isoleucine</td><td>0.97 g</td></tr>
    <tr><td>Leucine</td><td>1.72 g</td></tr>
    <tr><td>Lysine</td><td>1.31 g</td></tr>
    <tr><td>Methionine</td><td>0.33 g</td></tr>
    <tr><td>Phenylalanine</td><td>1.25 g</td></tr>
    <tr><td>Proline</td><td>1.42 g</td></tr>
    <tr><td>Serine</td><td>1.32 g</td></tr>
    <tr><td>Threonine</td><td>0.82 g</td></tr>
    <tr><td>Tryptophan</td><td>0.22 g</td></tr>
    <tr><td>Tyrosine</td><td>0.97 g</td></tr>
    <tr><td>Valine</td><td>1.12 g</td></tr>
  </table>
</section>

<div class="abs image-area-label">Image<br>Area<br>234.125mm</div>
<div class="abs height-label">238.125mm</div>

</body>
</html>
```